Email Template Design For Lumora Pathway Platform

I need an email ad template for sending out special offers to my customer email list. It has to work with Lumora Pathway. It needs to have an area for a product image, a description area, etc. The design should allow me to customize/change out the image and descriptions within the Lumora Pathways platform. I have attached a bad example of an ad for my first email blast. There will need to be URL links to take the customer to our website.

Target Market(s)

B to B Lab Supplies and Equipment Buyers

Industry/Entity Type

Life Science and Industrial Laboratories

Font styles to use
Sans Serif

Requirements
Must have
• Project must work within Lumora Pathway and allow user changeable images and descriptions
Nice to have
• I'm looking for a template that allows me to insert new content and images for any new campaign

```html
<!DOCTYPE html>
<html lang="en">
<head>
<meta charset="utf-8">
<title>Halvern Laboratory Supply – Special Offer</title>
<link href="https://fonts.googleapis.com/css2?family=Lato:wght@400;700;900&family=Montserrat:wght@600;800&display=swap" rel="stylesheet">
<style>
  :root {
    --ink: #111111;
    --body-grey: #555555;
    --contact-ink: #222222;
    --royal: #3347f0;
    --violet: #7a5cf0;
    --sky: #5ec4fb;
    --sky-panel: #5fc5fc;
    --product-bg: #e7edf3;
    --link: #48a6e6;
    --white: #ffffff;
  }
  * { margin: 0; padding: 0; box-sizing: border-box; }
  html, body { width: 1200px; height: 5286px; overflow: hidden; background: var(--white); }
  body { position: relative; font-family: "Lato", Arial, sans-serif; color: var(--ink); }

  .brand { position: absolute; top: 44px; left: 0; width: 1200px; display: flex; justify-content: center; align-items: center; gap: 28px; }
  .brand-mark { width: 110px; height: 110px; border-radius: 50%; background: var(--royal); }
  .brand-name { font-family: "Montserrat", Arial, sans-serif; font-weight: 800; color: var(--ink); line-height: 1.05; }
  .brand-name .line-1 { display: block; font-size: 56px; letter-spacing: 3px; }
  .brand-name .line-2 { display: block; font-size: 26px; letter-spacing: 1px; }
  .brand-meta { position: absolute; top: 168px; left: 0; width: 1200px; text-align: center; font-family: "Montserrat", Arial, sans-serif; font-weight: 600; font-size: 22px; word-spacing: 4px; }
  .brand-meta span + span { margin-left: 22px; }

  .hero { position: absolute; top: 0; left: 0; }

  .welcome { position: absolute; top: 1430px; left: 0; width: 1200px; text-align: center; }
  .welcome h1 { font-family: "Lato", Arial, sans-serif; font-weight: 900; font-size: 96px; letter-spacing: -1px; line-height: 1; color: var(--ink); }
  .welcome p { width: 1040px; margin: 0 auto; font-size: 53px; line-height: 76px; color: var(--body-grey); }
  .welcome p.first { margin-top: 38px; }
  .welcome p.second { margin-top: 76px; }

  .product { position: absolute; top: 2258px; left: 92px; width: 1016px; height: 800px; background: var(--product-bg); }
  .product svg { display: block; }

  .offer { position: absolute; top: 3056px; left: 92px; width: 1016px; height: 904px; background: var(--sky-panel); color: var(--white); text-align: center; }
  .offer-label { position: absolute; top: 42px; width: 100%; font-size: 66px; font-weight: 400; }
  .offer-amount { position: absolute; top: 140px; width: 100%; font-weight: 900; font-size: 222px; line-height: 200px; letter-spacing: -6px; }
  .offer-segment { position: absolute; top: 578px; width: 100%; font-size: 70px; }
  .offer-button { position: absolute; top: 720px; left: 316px; width: 386px; height: 128px; border-radius: 64px; background: var(--royal); color: var(--white); font-weight: 700; font-size: 40px; line-height: 128px; text-decoration: none; }

  .contacts { position: absolute; top: 4074px; left: 92px; list-style: none; }
  .contact { position: relative; height: 150px; margin-bottom: 50px; display: flex; align-items: center; }
  .contact-icon { width: 150px; height: 150px; border-radius: 26px; display: flex; align-items: center; justify-content: center; flex: none; }
  .contact-icon.royal { background: var(--royal); }
  .contact-icon.violet { background: var(--violet); }
  .contact-icon.sky { background: var(--sky); }
  .contact-text { margin-left: 50px; font-size: 54px; line-height: 70px; font-weight: 700; color: var(--contact-ink); }

  .footnote { position: absolute; top: 4940px; left: 0; width: 1200px; text-align: center; font-size: 35px; line-height: 57px; color: #333; }
  .footnote a { color: var(--link); text-decoration: underline; }

  .legal-bar { position: absolute; top: 5175px; left: 0; width: 1200px; height: 111px; background: var(--royal); color: var(--white); text-align: center; font-size: 35px; line-height: 60px; }
  .legal-bar .code { position: absolute; right: 22px; top: 40px; font-size: 20px; line-height: 20px; }
</style>
</head>
<body>

<header class="brand">
  <div class="brand-mark"></div>
  <div class="brand-name"><span class="line-1">HALVERN</span><span class="line-2">LABORATORY SUPPLY</span></div>
</header>
<div class="brand-meta"><span>www.goHalvernLab.com</span><span>800-555-0148</span></div>

<svg class="hero" width="1200" height="1400" viewBox="0 0 1200 1400">
  <defs>
    <radialGradient id="heroTop" cx="0.42" cy="0.38" r="0.75"><stop offset="0" stop-color="#b3bdfb"/><stop offset="0.45" stop-color="#7485f6"/><stop offset="1" stop-color="#3648e6"/></radialGradient>
    <radialGradient id="heroLeft" cx="0.6" cy="0.35" r="0.8"><stop offset="0" stop-color="#c2b8fb"/><stop offset="0.45" stop-color="#8474f3"/><stop offset="1" stop-color="#4f3fe0"/></radialGradient>
    <radialGradient id="heroRight" cx="0.45" cy="0.4" r="0.8"><stop offset="0" stop-color="#a9d8f7"/><stop offset="0.5" stop-color="#4c9ee6"/><stop offset="1" stop-color="#1d62b8"/></radialGradient>
  </defs>
  <polygon role="img" aria-label="Scientist in protective suit looking into a microscope" fill="url(#heroTop)" points="597,215 882,379 882,707 597,872 312,707 312,379"/>
  <polygon role="img" aria-label="Researcher in protective hood and goggles" fill="url(#heroLeft)" points="304,728 589,892 589,1221 304,1385 20,1221 20,892"/>
  <polygon role="img" aria-label="Lab technician holding a flask of liquid" fill="url(#heroRight)" points="895,728 1179,892 1179,1221 895,1385 611,1221 611,892"/>
</svg>

<section class="welcome">
  <h1>WELCOME</h1>
  <p class="first">At our store, we're proud to offer a wide range of Bacon Bomb Samplers in all sizes and shapes. So why wait?</p>
  <p class="second">Head over to our website now and browse our selection of Bacon Bomb Samplers. With our unbeatable prices, you're sure to find the perfect one for your application.</p>
</section>

<div class="product">
  <svg width="1016" height="800" viewBox="0 0 1016 800" role="img" aria-label="Stainless steel bacon bomb sampler with special offer tag">
    <defs>
      <linearGradient id="productTone" x1="0.05" y1="0.95" x2="0.95" y2="0.1">
        <stop offset="0" stop-color="#e9eff5"/>
        <stop offset="0.3" stop-color="#c9d0d8"/>
        <stop offset="0.5" stop-color="#8f98a3"/>
        <stop offset="0.7" stop-color="#c9d0d8"/>
        <stop offset="1" stop-color="#e9eff5"/>
      </linearGradient>
    </defs>
    <rect width="1016" height="800" fill="url(#productTone)"/>
  </svg>
</div>

<section class="offer">
  <div class="offer-label">HALVERN OFFER</div>
  <div class="offer-amount">20 %<br>OFF</div>
  <div class="offer-segment">B to B Lab Supplies</div>
  <a class="offer-button" href="#">CLICK HERE</a>
</section>

<ul class="contacts">
  <li class="contact">
    <div class="contact-icon royal">
      <svg width="64" height="56" viewBox="0 0 64 56"><path fill="#fff" d="M0 8 L20 0 L44 8 L64 0 V48 L44 56 L20 48 L0 56 Z M22 6 V46 L42 52 V12 Z" fill-rule="evenodd"/></svg>
    </div>
    <div class="contact-text">Address: 1420 Alder Crest Road<br>Brookfield, TX 77590 USA</div>
  </li>
  <li class="contact">
    <div class="contact-icon violet">
      <svg width="58" height="44" viewBox="0 0 58 44"><rect x="0" y="0" width="58" height="44" rx="5" fill="#fff"/><path d="M3 5 L29 24 L55 5" fill="none" stroke="#7a5cf0" stroke-width="5"/></svg>
    </div>
    <div class="contact-text">Email: websales@gohalvernlab.com</div>
  </li>
  <li class="contact">
    <div class="contact-icon sky">
      <svg width="56" height="56" viewBox="0 0 24 24"><path fill="#fff" d="M6.6 10.8a15.1 15.1 0 0 0 6.6 6.6l2.2-2.2a1 1 0 0 1 1-.25 11.4 11.4 0 0 0 3.6.57 1 1 0 0 1 1 1V20a1 1 0 0 1-1 1A17 17 0 0 1 3 4a1 1 0 0 1 1-1h3.5a1 1 0 0 1 1 1c0 1.25.2 2.45.57 3.57a1 1 0 0 1-.25 1z"/></svg>
    </div>
    <div class="contact-text">Phone: 800-555-0148</div>
  </li>
  <li class="contact">
    <div class="contact-icon royal">
      <svg width="60" height="60" viewBox="0 0 60 60" fill="none"><circle cx="30" cy="30" r="26" fill="#fff"/><g stroke="#3347f0" stroke-width="4"><ellipse cx="30" cy="30" rx="11" ry="26"/><line x1="4" y1="30" x2="56" y2="30"/><line x1="8" y1="17" x2="52" y2="17"/><line x1="8" y1="43" x2="52" y2="43"/></g></svg>
    </div>
    <div class="contact-text">Website URL<br>www.goHalvernLab.com</div>
  </li>
</ul>

<footer class="footnote">
  <p>You are receiving this email because you have visited our site<br>or asked us about the regular newsletter.</p>
  <p><a href="#">Terms and Conditions | Privacy Policy | Unsubscribe</a></p>
</footer>

<div class="legal-bar">© 2024 Halvern Laboratory Supply | All rights reserved.<span class="code">C9</span></div>

</body>
</html>
```